Larkmoor Health- Core Values Graphic for Visual Appeal

I would like a poster that could take these written core values from our organization and create a graphic that we could use for our staff and employees. I would also like to incorporate our branding into this project. Thank you!

Target Market(s)

To helps patients and employees understand the core values of our organization

Industry/Entity Type

Healthcare

Requirements
Must have
• Match our branding
Nice to have
• Please use your creativity!
Should not have
• Overly complex/ busy

```html
<!DOCTYPE html>
<html lang="en">
<head>
<meta charset="utf-8">
<title>Larkmoor Health – Core Values</title>
<link href="https://fonts.googleapis.com/css2?family=Exo+2:wght@400;500&family=Ubuntu:wght@500;700&display=swap" rel="stylesheet">
<style>
  :root {
    --page: #e9e9ea;
    --panel-dark: #5d5e61;
    --photo-top: #c6c9cd;
    --photo-mid: #dcdee1;
    --photo-low: #cfd6dc;
    --band-deep: #3595c9;
    --band-bright: #46b0e3;
    --icon-disc: #4a4b4e;
    --white: #ffffff;
    --brand-blue: #2aa6e3;
  }
  * { box-sizing: border-box; margin: 0; padding: 0; }
  html, body {
    width: 927px; height: 1200px; overflow: hidden;
    background: var(--page);
  }
  .poster {
    position: absolute; left: 26px; top: 34px;
    width: 874px; height: 1130px; overflow: hidden;
    background: var(--panel-dark);
    font-family: "Exo 2", sans-serif;
    color: var(--white);
  }
  .photo {
    position: absolute; left: 546px; top: 0; width: 328px; height: 100%;
    background: linear-gradient(180deg, var(--photo-top) 0%, var(--photo-mid) 40%, var(--photo-low) 70%, var(--photo-mid) 100%);
  }
  .panel-tint {
    position: absolute; left: 0; top: 0; width: 546px; height: 100%;
    background: linear-gradient(180deg, #5a5b5e 0%, #636467 50%, #5b5c5f 100%);
  }
  .brand {
    position: absolute; left: 0; width: 546px; top: 120px;
    display: flex; align-items: center; justify-content: center; gap: 12px;
  }
  .brand-dot {
    width: 26px; height: 26px; border-radius: 50%; background: var(--brand-blue);
  }
  .brand-name {
    font-family: "Exo 2", sans-serif; font-weight: 500;
    font-size: 34px; color: var(--brand-blue); letter-spacing: 0.5px;
  }
  .intro {
    position: absolute; left: 64px; width: 418px; top: 316px;
    font-size: 16.5px; line-height: 20px; text-align: center;
  }
  .value {
    position: absolute; left: 79px; width: 795px; height: 128px;
    border-radius: 64px 0 0 64px;
    background: linear-gradient(90deg, var(--band-deep) 0%, #3a9fd4 55%, var(--band-bright) 100%);
  }
  .value--family { top: 467px; }
  .value--excellence { top: 620px; }
  .value--integrity { top: 772px; }
  .value--service { top: 925px; }
  .value-icon {
    position: absolute; left: 22px; top: 15px;
    width: 98px; height: 98px; border-radius: 50%;
    background: var(--icon-disc);
    display: flex; align-items: center; justify-content: center;
  }
  .value-icon svg { width: 62px; height: 62px; }
  .value-title {
    position: absolute; left: 137px; top: 14px;
    font-family: "Ubuntu", sans-serif; font-weight: 700;
    font-size: 26px; line-height: 30px;
  }
  .value-text {
    position: absolute; left: 139px; top: 53px; width: 600px;
    font-size: 13.2px; line-height: 14.4px; text-align: justify;
  }
</style>
</head>
<body>
  <main class="poster">
    <div class="photo" role="img" aria-label="Photo of a healthcare worker in protective cap, goggles and mask, with faint medical cross icons"></div>
    <div class="panel-tint"></div>

    <div class="brand">
      <span class="brand-dot"></span>
      <span class="brand-name">Larkmoor Health</span>
    </div>

    <p class="intro">These core values are the spirit of who we are as a healthcare team. They guide our actions, unite us in purpose, and ensure that we provide world-class care while fostering a positive and supportive atmosphere within our team:</p>

    <section class="value value--family">
      <div class="value-icon">
        <svg viewBox="0 0 64 64" fill="#fff" aria-hidden="true">
          <circle cx="18" cy="12" r="7"/><circle cx="46" cy="12" r="7"/>
          <path d="M8 24q0-4 5-4h10q5 0 5 4v16h-4v18h-12v-18h-4z"/>
          <path d="M36 24q0-4 5-4h10q5 0 5 4v16h-4v18h-12v-18h-4z"/>
          <circle cx="32" cy="28" r="6" stroke="#4a4b4e" stroke-width="2"/>
          <path d="M24 40q0-4 4-4h8q4 0 4 4v8h-3v12h-10v-12h-3z" stroke="#4a4b4e" stroke-width="2"/>
        </svg>
      </div>
      <h2 class="value-title">Family</h2>
      <p class="value-text">At the heart of our mission is the commitment to provide high-quality, affordable healthcare in a comforting and uplifting family-oriented environment. Just as our community is our extended family, every patient is a cherished member of our healthcare family. We treat each individual with the same care, compassion, and respect we would offer to our own loved ones.</p>
    </section>

    <section class="value value--excellence">
      <div class="value-icon">
        <svg viewBox="0 0 64 64" fill="#fff" aria-hidden="true">
          <path d="M32 2l5 9 10 2-7 7 2 10-10-5-10 5 2-10-7-7 10-2z"/>
          <path d="M14 22q-2 14 8 22l-2 12h24l-2-12q10-8 8-22l-6 2q0 10-8 12q-8-2-8-12z"/>
          <rect x="12" y="56" width="40" height="6"/>
        </svg>
      </div>
      <h2 class="value-title">Excellence</h2>
      <p class="value-text">In line with our goal, we aspire not only to alleviate pain but also to inspire patients to become active participants in their well-being. We believe in empowering our patients through education and compassion. Our pursuit of excellence is unwavering, driven by our dedication to continuously improve our services at every level, ensuring that our community receives nothing less than exceptional care.</p>
    </section>

    <section class="value value--integrity">
      <div class="value-icon">
        <svg viewBox="0 0 64 64" fill="#fff" aria-hidden="true">
          <circle cx="32" cy="32" r="30"/>
          <path d="M32 2v60M2 32h60" stroke="#4a4b4e" stroke-width="3"/>
          <circle cx="32" cy="18" r="5" fill="#4a4b4e"/>
          <circle cx="46" cy="32" r="5" fill="#4a4b4e"/>
          <circle cx="18" cy="32" r="5" fill="#fff"/>
          <circle cx="32" cy="46" r="5" fill="#fff"/>
        </svg>
      </div>
      <h2 class="value-title">Integrity</h2>
      <p class="value-text">In our healthcare team, 'Integrity' is non-negotiable. Our purpose is deeply rooted in ethics, integrity, and professional standards. We operate with the utmost integrity in every aspect of our work, adhering to the highest ethical principles. We understand that trust is the foundation of healthcare, and we are committed to maintaining the trust our community places in us.</p>
    </section>

    <section class="value value--service">
      <div class="value-icon">
        <svg viewBox="0 0 64 64" aria-hidden="true">
          <circle cx="32" cy="32" r="20" fill="none" stroke="#fff" stroke-width="8"/>
          <g fill="#fff">
            <rect x="28" y="4" width="8" height="10"/><rect x="28" y="50" width="8" height="10"/>
            <rect x="4" y="28" width="10" height="8"/><rect x="50" y="28" width="10" height="8"/>
            <rect x="28" y="4" width="8" height="10" transform="rotate(45 32 32)"/>
            <rect x="28" y="4" width="8" height="10" transform="rotate(-45 32 32)"/>
            <rect x="28" y="50" width="8" height="10" transform="rotate(45 32 32)"/>
            <rect x="28" y="50" width="8" height="10" transform="rotate(-45 32 32)"/>
            <path d="M22 18v10q0 6 6 8v22h8v-22q6-2 6-8v-10h-5v9h-10v-9z"/>
          </g>
        </svg>
      </div>
      <h2 class="value-title">Service</h2>
      <p class="value-text">Our vision is grounded in the belief that every person possesses the innate potential for true health. We aim to facilitate the body's natural healing response by providing the highest level of service. Our hope for each patient extends beyond healing; we aspire to help you fulfill your life's mission and purpose abundantly, supporting you in your journey to well-being.</p>
    </section>
  </main>
</body>
</html>
```